REAL ESTATE MAILBOX DROP FLYER

I am looking for two flyer designs. One for DL and one for A4 size. My company is a boutique real estate agency that offers a full/high quality service at a very low commission rate.

Key Phrases to be included

A4 Design should have a space for some text and a table in the center (outline below)

Target Market(s)

Home Owners

Industry/Entity Type

Real Estate Agent

Colors
0455a3

Requirements
Must have
• Eye Catching
• Bold
• high end feel
• Color pallette should match the logo
• The feel of the brochures must convey a trustworthy, high end service.
• Must be eye catching and easy to read
• Editable file formats must be supplied

```html
<!DOCTYPE html>
<html lang="en">
<head>
<meta charset="utf-8">
<title>Tenth Lane Realty – DL Flyer</title>
<link href="https://fonts.googleapis.com/css2?family=Chakra+Petch:ital,wght@0,600;0,700;1,600;1,700&family=Open+Sans:wght@400;700&display=swap" rel="stylesheet">
<style>
  :root {
    --brand-blue: #0455a3;
    --deep-blue: #0a3c9c;
    --text-blue: #1441ad;
    --band-blue: #0b48b2;
    --badge-red: #e4262d;
    --navy: #1e2a44;
    --ink: #141414;
    --paper: #ffffff;
    --backdrop: #e4e5e7;
  }
  * { margin: 0; padding: 0; box-sizing: border-box; }
  html, body { width: 1200px; height: 841px; overflow: hidden; background: var(--backdrop); }
  .flyer {
    position: absolute; left: 410px; top: 20px;
    width: 380px; height: 800px;
    background: var(--paper);
    overflow: hidden;
    box-shadow: 0 6px 18px rgba(0,0,0,.18);
    font-family: "Open Sans", sans-serif;
  }
  .flyer-art { position: absolute; inset: 0; }
  .brand-name {
    position: absolute; left: 26px; top: 30px;
    font-family: "Chakra Petch", sans-serif; font-weight: 700;
    font-size: 25px; line-height: 1.05; letter-spacing: 1px;
    color: var(--navy); text-transform: uppercase;
  }
  .offer-badge {
    position: absolute; left: 148px; top: 132px;
    width: 182px; height: 78px;
    background: var(--badge-red); border: 2px solid #fff; border-radius: 8px;
    color: #fff; text-align: center;
    box-shadow: 0 2px 6px rgba(0,0,0,.25);
  }
  .offer-badge .offer-line { font-family: "Chakra Petch", sans-serif; font-weight: 700; font-size: 14px; margin-top: 6px; }
  .offer-badge .offer-rate { font-family: "Chakra Petch", sans-serif; font-weight: 700; font-size: 20px; line-height: 1; }
  .offer-badge .offer-word { font-size: 20px; letter-spacing: 1.5px; line-height: 1.2; }
  .call-to-action {
    position: absolute; left: 22px; top: 560px;
    font-family: "Chakra Petch", sans-serif; font-style: italic; font-weight: 700;
    color: var(--text-blue); text-transform: uppercase; line-height: 1.05;
  }
  .cta-label { font-size: 15px; font-weight: 600; }
  .cta-name { font-size: 33px; }
  .cta-appraisal { font-size: 24px; }
  .cta-saving { font-size: 15px; font-weight: 600; margin-top: 3px; }
  .contact-band {
    position: absolute; left: 0; top: 702px; width: 380px; height: 22px;
    background: var(--band-blue); color: #fff;
    font-family: "Chakra Petch", sans-serif; font-style: italic; font-weight: 700;
    font-size: 13px; line-height: 22px; text-align: center; text-transform: uppercase;
  }
  .contact-list { position: absolute; left: 24px; top: 730px; list-style: none; color: var(--ink); font-size: 15px; line-height: 21px; }
  .contact-list li { display: flex; align-items: center; gap: 9px; }
  .contact-list svg { width: 12px; height: 12px; flex: none; fill: var(--navy); }
  .contact-list strong { font-weight: 700; }
</style>
</head>
<body>
  <div class="flyer">
    <svg class="flyer-art" viewBox="0 0 380 800" width="380" height="800">
      <defs>
        <linearGradient id="panelBlue" x1="0" y1="0" x2="0.4" y2="1">
          <stop offset="0" stop-color="#1d63c6"/>
          <stop offset="1" stop-color="#0a3c9c"/>
        </linearGradient>
        <linearGradient id="livingTones" x1="0" y1="0" x2="0.3" y2="1">
          <stop offset="0" stop-color="#e3e5e7"/>
          <stop offset="0.55" stop-color="#b9b7b2"/>
          <stop offset="1" stop-color="#8c6a55"/>
        </linearGradient>
        <linearGradient id="bedroomTones" x1="0" y1="0" x2="0" y2="1">
          <stop offset="0" stop-color="#e9eaec"/>
          <stop offset="0.6" stop-color="#c9ccd2"/>
          <stop offset="1" stop-color="#4a4a4e"/>
        </linearGradient>
        <linearGradient id="loungeTones" x1="0" y1="0" x2="0" y2="1">
          <stop offset="0" stop-color="#dcdde0"/>
          <stop offset="0.55" stop-color="#c8c4bd"/>
          <stop offset="1" stop-color="#b98a52"/>
        </linearGradient>
      </defs>
      <polygon class="blue-panel" points="0,128 255,128 0,470" fill="url(#panelBlue)"/>
      <polygon class="photo-living" role="img" aria-label="Photo of a bright living and dining room with a round white table and grey sofa"
               points="282,78 380,78 380,330 62,346" fill="url(#livingTones)"/>
      <polygon class="photo-bedroom" role="img" aria-label="Photo of a bedroom with a made bed, dark carpet and window"
               points="42,354 376,338 232,528 0,542" fill="url(#bedroomTones)"/>
      <polygon class="blue-accent" points="332,430 380,424 380,506 266,512" fill="var(--band-blue)"/>
      <polygon class="photo-lounge" role="img" aria-label="Photo of a lounge room with sofas, woven rug and plants"
               points="272,524 380,518 380,700 150,700" fill="url(#loungeTones)"/>
    </svg>

    <div class="brand-name">Tenth Lane<br>Realty</div>

    <div class="offer-badge">
      <div class="offer-line">FULL SERVICE AGENCY,</div>
      <div class="offer-rate">1%</div>
      <div class="offer-word">Commission</div>
    </div>

    <div class="call-to-action">
      <div class="cta-label">Contact</div>
      <div class="cta-name">Marcus Ellery</div>
      <div class="cta-appraisal">For a free appraisal!</div>
      <div class="cta-saving">Save thousands on commissions!</div>
    </div>

    <div class="contact-band">Contact details:&nbsp; More money in your pocket!</div>

    <ul class="contact-list">
      <li><svg viewBox="0 0 24 24"><path d="M6.6 10.8a15 15 0 0 0 6.6 6.6l2.2-2.2a1 1 0 0 1 1-.25 11.4 11.4 0 0 0 3.6.57 1 1 0 0 1 1 1V20a1 1 0 0 1-1 1A17 17 0 0 1 3 4a1 1 0 0 1 1-1h3.5a1 1 0 0 1 1 1c0 1.25.2 2.45.57 3.57a1 1 0 0 1-.25 1z"/></svg><span>Marcus Ellery - <strong>0400 218 736</strong></span></li>
      <li><svg viewBox="0 0 24 24"><path d="M2 5h20v14H2z M2 5l10 8 10-8" fill="none" stroke="#1e2a44" stroke-width="2.5"/></svg><span>marcus@tenthlanerealty.com.au</span></li>
      <li><svg viewBox="0 0 24 24"><circle cx="12" cy="12" r="10" fill="none" stroke="#1e2a44" stroke-width="2.5"/><path d="M2 12h20M12 2c3 3 3 17 0 20M12 2c-3 3-3 17 0 20" fill="none" stroke="#1e2a44" stroke-width="2"/></svg><span>www.tenthlanerealty.com.au</span></li>
    </ul>
  </div>
</body>
</html>
```